Consultant needs a simple webpage with WOW effect

I educate advisors in the financial sector in the use of Meetra, Talvo, ScreenLink etc. for online customer meetings.
My Company has a name (Vaneo) and a domain (vaneo.dk).
VANEO is VArige NEtOpgaver (digital competences in Danish)
I made a terrible mock up via the editor on plixo.com on the domain. Have a look.
I need my logo to be much better (but I would like to keep the 0II0) and the webpage to be totally re-designed and catchy.
The text is in Danish and the headlines is what, how and who (Hvem, hvad og hvordan).
Ideas for a better structure are welcome :-)

Target Group: Human Ressource, technical developers and business developers in financial Companies. In Denmark we do not have a tradition for very "corporate" looks in the finansial sector. I would like creativity and customer value to be on top of mind.

Task: Redesign the logo, design the web page.

```html
<!DOCTYPE html>
<html lang="da">
<head>
<meta charset="utf-8">
<title>Vaneo – Varige Netopgaver</title>
<link rel="stylesheet" href="https://fonts.googleapis.com/css2?family=PT+Sans:wght@400;700&family=PT+Sans+Narrow:wght@400;700&display=swap">
<style>
  :root {
    --orange: #e2690f;
    --orange-light: #ee8a2a;
    --black: #000;
    --cream: #f1ede5;
    --card: #f8f7f5;
    --ink: #1c1c1c;
    --muted: #7a7a7a;
    --link-blue: #2a4a8a;
    --white: #fff;
  }
  * { box-sizing: border-box; margin: 0; padding: 0; }
  html, body { width: 741px; height: 1200px; overflow: hidden; }
  body {
    position: relative;
    background: var(--cream);
    font-family: "PT Sans", sans-serif;
    color: var(--ink);
  }
  .abs { position: absolute; }
  .narrow { font-family: "PT Sans Narrow", sans-serif; }

  /* Header */
  .topbar { left: 0; top: 0; width: 741px; height: 17px; background: var(--orange); }
  .topbar-phone { right: 22px; top: 1px; color: var(--white); font-size: 13px; }
  .hero {
    left: 0; top: 0; width: 741px; height: 311px;
    background: linear-gradient(135deg, #8f99a6 0%, #d9dde2 35%, #eef0f2 60%, #b8c2cf 100%);
  }
  .navband { left: 0; top: 17px; width: 741px; height: 32px; background: rgba(255,255,255,.88); }
  .mainnav { top: 25px; left: 254px; display: flex; gap: 0; font-size: 12px; color: var(--ink); }
  .mainnav span { margin-right: 26px; }
  .brand {
    left: 63px; top: 0; width: 158px; height: 89px; background: var(--black);
    display: flex; flex-direction: column; align-items: center; justify-content: center; gap: 6px;
  }
  .brand-name { color: var(--orange); font-size: 28px; font-weight: 400; letter-spacing: 1px; }
  .brand-sub { color: var(--white); font-size: 8px; letter-spacing: .5px; }
  .hero-caption {
    left: 63px; top: 158px; width: 271px; height: 84px; background: rgba(40,40,40,.78);
    color: var(--white); font-size: 25px; line-height: 31px; padding: 10px 0 0 21px;
  }

  /* Intro */
  .band { left: 0; top: 311px; width: 741px; height: 75px; background: var(--orange); }
  .why {
    left: 81px; top: 311px; width: 135px; height: 481px; background: var(--orange); color: var(--white);
    clip-path: polygon(0 0, 100% 0, 100% 450px, 50% 100%, 0 450px);
    text-align: center;
  }
  .why-mark { margin-top: 22px; font-size: 20px; font-weight: 700; letter-spacing: 1px; }
  .why-icon { margin-top: 18px; }
  .why h2 { font-size: 18px; font-weight: 400; margin-top: 4px; }
  .why-lead { font-size: 10px; line-height: 14px; margin-top: 6px; font-family: "PT Sans Narrow", sans-serif; }
  .why-lead b { font-size: 15px; line-height: 18px; font-family: "PT Sans", sans-serif; display: block; }
  .why ul { list-style: none; text-align: left; margin: 18px 0 0 9px; font-size: 9.5px; line-height: 12px; }
  .why li { position: relative; padding-left: 16px; margin-bottom: 13px; }
  .why li svg { position: absolute; left: 0; top: 2px; }

  .card {
    top: 338px; width: 134px; height: 224px; background: var(--card); padding: 10px 9px 0;
  }
  .card-photo { width: 116px; height: 86px; }
  .card h3 { text-align: center; font-size: 18px; font-weight: 400; margin-top: 14px; }
  .card p { font-size: 9.5px; line-height: 12px; margin-top: 18px; padding: 0 2px; }
  .card .more { position: absolute; right: 10px; bottom: 6px; }

  /* About */
  .about { left: 0; top: 570px; width: 741px; height: 254px; background: var(--black); color: var(--white); }
  .about h2 { position: absolute; left: 247px; top: 17px; font-size: 19px; font-weight: 400; }
  .about-lead { position: absolute; left: 247px; top: 44px; font-size: 13px; }
  .about-photo { position: absolute; left: 245px; top: 76px; width: 151px; height: 128px; }
  .about-body { position: absolute; left: 414px; top: 74px; width: 245px; font-size: 9.5px; line-height: 12px; }
  .about-body p + p { margin-top: 12px; }

  /* Testimonials + news */
  .section-title { font-size: 19px; font-weight: 400; color: var(--ink); }
  .arrows { top: 855px; left: 402px; color: var(--link-blue); font-size: 18px; word-spacing: 18px; }
  .quote { left: 98px; top: 891px; width: 353px; height: 106px; background: var(--white); border-radius: 16px; padding: 22px 38px; }
  .quote-tail { left: 77px; top: 910px; }
  .quote p { font-size: 13.5px; line-height: 18px; color: #2a2a2a; }
  .quote .client { font-size: 11.5px; color: var(--muted); margin-top: 8px; line-height: 14px; }
  .news-date { left: 483px; top: 894px; color: var(--orange); font-size: 11px; font-weight: 700; }
  .news-body { left: 483px; top: 913px; width: 190px; font-size: 9.5px; line-height: 12px; color: #2a2a2a; }
  .news-more { left: 483px; top: 975px; font-size: 9.5px; font-weight: 700; }
  .cta { left: 0; top: 1012px; width: 741px; text-align: center; color: var(--orange); font-size: 29px; font-weight: 700; }

  /* Footer */
  .rule { left: 0; top: 1054px; width: 741px; height: 6px; background: var(--orange); }
  .footer { left: 0; top: 1060px; width: 741px; height: 96px; background: var(--black); }
  .footnav { position: absolute; top: 17px; left: 198px; display: flex; font-size: 8px; color: var(--white); }
  .footnav span { margin-right: 26px; }
  .social { position: absolute; top: 53px; left: 311px; display: flex; gap: 4px; }
  .social i { width: 20px; height: 20px; border-radius: 50%; background: var(--white); display: block; }
  .copyright { left: 0; top: 1165px; width: 741px; text-align: center; font-size: 11px; color: #3a4c6a; }
</style>
</head>
<body>
  <div class="abs hero" role="img" aria-label="Photo of advisors at a desk reviewing financial charts with a pen"></div>
  <div class="abs topbar"></div>
  <div class="abs topbar-phone">Call Us Now 1100 222 333</div>
  <div class="abs navband"></div>
  <nav class="abs mainnav">
    <span>About Us</span><span>What</span><span>How</span><span>Who</span><span>Testimonial</span><span>News</span><span>Contact Us</span>
  </nav>
  <div class="abs brand">
    <div class="brand-name">VANEO</div>
    <div class="brand-sub">VARIGE NETOPGAVER</div>
  </div>
  <div class="abs hero-caption narrow">EDUCATE ADVISORS IN<br>THE FINANCIAL SECTOR</div>

  <div class="abs band"></div>

  <aside class="abs why">
    <div class="why-mark">VANEO</div>
    <svg class="why-icon" width="54" height="50" viewBox="0 0 54 50" aria-hidden="true">
      <rect x="2" y="2" width="50" height="36" fill="none" stroke="#000" stroke-width="4"/>
      <rect x="22" y="38" width="10" height="7" fill="#000"/>
      <rect x="14" y="45" width="26" height="4" fill="#000"/>
    </svg>
    <h2 class="narrow">WHY US</h2>
    <div class="why-lead">I educate advisors in the financial sector in the use of
      <b>Meetra,<br>Talvo,<br>ScreenLink etc.</b>
      for online customer meetings.</div>
    <ul>
      <li><svg width="10" height="9" viewBox="0 0 10 9"><path d="M1 5l3 3 5-7" fill="none" stroke="#fff" stroke-width="2"/></svg>Loren involving the funding of capital</li>
      <li><svg width="10" height="9" viewBox="0 0 10 9"><path d="M1 5l3 3 5-7" fill="none" stroke="#fff" stroke-width="2"/></svg>Loren text Equipment</li>
      <li><svg width="10" height="9" viewBox="0 0 10 9"><path d="M1 5l3 3 5-7" fill="none" stroke="#fff" stroke-width="2"/></svg>Loren text ithin an office environment and then</li>
      <li><svg width="10" height="9" viewBox="0 0 10 9"><path d="M1 5l3 3 5-7" fill="none" stroke="#fff" stroke-width="2"/></svg>Lorne textuild documentation around the solution</li>
    </ul>
  </aside>

  <article class="abs card" style="left:229px">
    <div class="card-photo" role="img" aria-label="Rolled banknotes and stacked coins" style="background:linear-gradient(135deg,#b7a890,#7d7468)"></div>
    <h3 class="narrow">WHAT</h3>
    <p>VANEO uddanner og træner rådgivere i den finansielle sektor i afholdelse af gode kundemøder på digitale platforme.</p>
    <svg class="more" width="12" height="10" viewBox="0 0 12 10"><path d="M1 1l4 4-4 4M6 1l4 4-4 4" fill="none" stroke="#e2690f" stroke-width="2"/></svg>
  </article>
  <article class="abs card" style="left:374px">
    <div class="card-photo" role="img" aria-label="Reading glasses on a calculator and printed spreadsheet" style="background:linear-gradient(135deg,#dfe6ee,#8ea2b8)"></div>
    <h3 class="narrow">HOW</h3>
    <p>VANEO uddanner og træner rådgivere i den finansielle sektor i afholdelse af gode kundemøder på digitale platforme.</p>
    <svg class="more" width="12" height="10" viewBox="0 0 12 10"><path d="M1 1l4 4-4 4M6 1l4 4-4 4" fill="none" stroke="#e2690f" stroke-width="2"/></svg>
  </article>
  <article class="abs card" style="left:520px">
    <div class="card-photo" role="img" aria-label="Business people shaking hands in an office" style="background:linear-gradient(135deg,#2a3346,#8e97a6)"></div>
    <h3 class="narrow">WHO</h3>
    <p>VANEO uddanner og træner rådgivere i den finansielle sektor i afholdelse af gode kundemøder på digitale platforme.</p>
    <svg class="more" width="12" height="10" viewBox="0 0 12 10"><path d="M1 1l4 4-4 4M6 1l4 4-4 4" fill="none" stroke="#e2690f" stroke-width="2"/></svg>
  </article>

  <section class="abs about">
    <h2 class="narrow">ABOUT US</h2>
    <div class="about-lead">Loren text here e look for solutions to complex problems involving</div>
    <div class="about-photo" role="img" aria-label="Businessman in a suit holding a laptop in a bright office" style="background:linear-gradient(135deg,#d8dde2,#6e7784)"></div>
    <div class="about-body">
      <p>Loren text here e look for solutions to complex problems involving the funding of capital equipment</p>
      <p>Within an office environment and then build documentation around the solution Within an office environment and then build documentation around the solution Within an office environment and then build documentation around the solution Within an office environment and then build documentation around the solution Within an office environment and then build</p>
    </div>
  </section>

  <h2 class="abs section-title narrow" style="left:87px;top:852px">WHAT PEOPLE SAY ABOUT US</h2>
  <div class="abs arrows">&lt; &gt;</div>
  <svg class="abs quote-tail" width="26" height="22" viewBox="0 0 26 22"><path d="M0 0L26 2 24 22Z" fill="#fff"/></svg>
  <div class="abs quote">
    <p>...very efficient dealing with all the necessary paperwork and found me the best deals</p>
    <div class="client">Client name<br>USA ...</div>
  </div>

  <h2 class="abs section-title narrow" style="left:484px;top:852px">NEWS AND EVENTS</h2>
  <div class="abs news-date">11 05 2014</div>
  <div class="abs news-body">We look for solutions to complex problems involving the funding of capital equipment within an office environment and then build documentation around the solution</div>
  <div class="abs news-more">Read More...</div>

  <div class="abs cta">Call Us Now 100 222 333</div>

  <div class="abs rule"></div>
  <footer class="abs footer">
    <nav class="footnav">
      <span>Home</span><span>About Us</span><span>What</span><span>How</span><span>Who</span><span>Testimonial</span><span>News</span><span>Contact Us</span>
    </nav>
    <div class="social"><i></i><i></i><i></i><i></i><i></i><i></i></div>
  </footer>
  <div class="abs copyright">©&nbsp; your company name here&nbsp; All rights reserved.</div>
</body>
</html>
```